Cinder Reef E-Liquid - We need four labels designed and a logo.

We need four labels designed for our eliquid line.
The labels should have some artwork showing the flavors of each of the liquids. The list below shows what they are. Also, we would like some type of logo design, that will keep the labels uniform.
Wobbly Crowns - a cinnamon toast cereal
Orange mango kiwi - Orange, mango, and kiwi.
Pink Tundra - Pink Tundra
Lima Plum - Fiji apple, watermelon, and guava.

Logo Text

Cinder Reef

Requirements
Must have
• The project must have the overlay I just uploaded.

```html
<!DOCTYPE html>
<html lang="en">
<head>
<meta charset="utf-8">
<title>Cinder Reef E-Liquid – Wobbly Crowns Label</title>
<link href="https://fonts.googleapis.com/css2?family=Lexend:wght@500;700&family=Roboto+Condensed:wght@400;700&family=Arimo:wght@400;700&display=swap" rel="stylesheet">
<style>
  :root {
    --page: #ffffff;
    --frame: #29a3dd;
    --brand-orange: #f4964d;
    --brand-deep: #d9561c;
    --haze: #f5f5f5;
    --ink: #111111;
    --warn-red: #d8262b;
    --box-line: #9a9a9a;
    --badge-blue: #2e6db3;
    --recycle-green: #1f9a3a;
    --navy: #1b2a5c;
  }
  * { box-sizing: border-box; margin: 0; padding: 0; }
  html, body { width: 1200px; height: 1200px; overflow: hidden; background: var(--page); }
  .canvas { position: relative; width: 1200px; height: 1200px; background: var(--page); }

  .label {
    position: absolute; left: 156px; top: 353px; width: 888px; height: 494px;
    border: 2px solid var(--frame); background: var(--page); overflow: hidden;
  }
  .side-divider { position: absolute; left: 132px; top: 0; bottom: 0; width: 1px; background: #f3f3f3; }

  .info-panel {
    position: absolute; left: 16px; top: 17px; width: 100px; height: 300px;
    writing-mode: vertical-rl;
    font-family: "Roboto Condensed", sans-serif; font-size: 9.6px; line-height: 15px; color: var(--ink);
  }
  .info-panel strong { font-weight: 700; }
  .info-panel p + p { margin-right: 2px; }

  .partner-badge { position: absolute; left: 50px; top: 243px; width: 72px; height: 50px; }

  .haze { position: absolute; left: 0; top: 0; }

  .brand-name {
    position: absolute; left: 0; width: 888px; top: 24px; text-align: center;
    font-family: "Lexend", sans-serif; font-weight: 700; font-size: 64px; letter-spacing: -1px;
    color: var(--brand-orange); line-height: 76px;
  }
  .flavor-art {
    position: absolute; left: 362px; top: 161px; width: 160px; height: 160px; border-radius: 50%;
    background: radial-gradient(circle at 40% 35%, #f6a25e, var(--brand-deep) 75%, #a33216);
  }

  .flavor-bar {
    position: absolute; left: 148px; top: 400px; width: 614px; height: 46px; border-radius: 23px;
    background: var(--brand-orange); color: #fff; text-align: center;
    font-family: "Lexend", sans-serif; font-weight: 700; font-size: 20px; line-height: 46px; letter-spacing: -0.8px;
  }
  .spec {
    position: absolute; top: 452px; width: 120px; margin-left: -60px; text-align: center;
    font-family: "Lexend", sans-serif; font-weight: 500; font-size: 21px; letter-spacing: -1px; color: var(--brand-orange);
  }
  .spec-strength { left: 362px; }
  .spec-volume { left: 525px; }

  .warning-box {
    position: absolute; left: 776px; top: 20px; width: 94px; height: 241px;
    border: 1px solid var(--box-line); border-radius: 3px;
    display: flex; align-items: center; justify-content: center;
  }
  .warning-text {
    writing-mode: vertical-rl; transform: rotate(180deg); text-align: center;
    font-family: "Arimo", sans-serif; font-size: 18px; line-height: 19px; color: var(--ink);
  }
  .warning-text .warning-head { color: var(--warn-red); font-size: 29px; line-height: 30px; }

  .icon { position: absolute; width: 28px; height: 28px; }
  .age-mark {
    position: absolute; width: 36px; height: 36px; border: 1px solid #f1c9c9; border-radius: 50%;
    font-family: "Arimo", sans-serif; font-weight: 700; font-size: 18px; line-height: 34px;
    text-align: center; letter-spacing: -1.5px; color: var(--ink);
  }
  .age-note {
    position: absolute; right: 12px; top: 394px; width: 120px; text-align: right;
    font-family: "Roboto Condensed", sans-serif; font-weight: 700; font-size: 7.6px; line-height: 10px; color: var(--ink);
  }
  .flag-art {
    position: absolute; left: 794px; top: 422px; width: 80px; height: 43px;
    background: linear-gradient(135deg, #2a3f8f 0 40%, #c9303a 40% 55%, #ffffff 55% 62%, #c9303a 62% 78%, #ffffff 78% 85%, #c9303a 85%);
  }
  .origin {
    position: absolute; left: 790px; top: 472px; width: 90px; text-align: center;
    font-family: "Arimo", sans-serif; font-weight: 700; font-size: 10px; letter-spacing: 0.8px; color: var(--navy);
  }
</style>
</head>
<body>
<div class="canvas">
  <div class="label">
    <div class="side-divider"></div>

    <div class="info-panel">
      <p><strong>Ingredients:</strong><br>USP Grade Glycerin, USP Grade Propylene Glycol,<br>Natural &amp; Artificial Flavoring, USP Grade Nicotine</p>
      <p><strong>Prop 65 Warning:</strong><br>This product may contain a chemical known to the state<br>of California to cause birth defects, or other reproductive harm.</p>
    </div>

    <svg class="partner-badge" viewBox="0 0 72 50" aria-hidden="true">
      <path d="M4 6 L36 1 L68 6 L68 30 Q52 46 36 49 Q20 46 4 30 Z" fill="var(--badge-blue)"/>
    </svg>

    <svg class="haze" width="888" height="494" aria-hidden="true">
      <g fill="var(--haze)">
        <rect x="182" y="138" width="56" height="22" rx="11"/>
        <rect x="262" y="138" width="102" height="22" rx="11"/>
        <rect x="540" y="138" width="86" height="22" rx="11"/>
        <rect x="650" y="138" width="56" height="22" rx="11"/>
        <rect x="170" y="183" width="547" height="22" rx="11"/>
        <rect x="250" y="252" width="57" height="22" rx="11"/>
        <rect x="330" y="252" width="34" height="22" rx="11"/>
        <rect x="524" y="252" width="34" height="22" rx="11"/>
        <rect x="581" y="252" width="57" height="22" rx="11"/>
        <rect x="318" y="294" width="246" height="22" rx="11"/>
        <rect x="352" y="319" width="184" height="22" rx="11"/>
        <rect x="330" y="343" width="229" height="22" rx="11"/>
      </g>
    </svg>

    <h1 class="brand-name">CINDER REEF</h1>
    <div class="flavor-art" role="img" aria-label="Brand emblem area in warm orange tones"></div>

    <div class="flavor-bar">WOBBLY CROWNS</div>
    <div class="spec spec-strength">03 mg</div>
    <div class="spec spec-volume">30 ml</div>

    <div class="warning-box">
      <p class="warning-text"><span class="warning-head">WARNING:</span><br>This product may contain<br>nicotine. Nicotine<br>is an addictive chemical.</p>
    </div>

    <svg class="icon" style="left:812px;top:278px" viewBox="0 0 28 28" aria-hidden="true">
      <path d="M14 2 L26 14 L14 26 L2 14 Z" fill="#fff" stroke="#e9a3a3" stroke-width="1.5"/>
    </svg>
    <svg class="icon" style="left:845px;top:278px" viewBox="0 0 28 28" aria-hidden="true">
      <circle cx="14" cy="14" r="12.5" fill="var(--recycle-green)"/>
    </svg>
    <svg class="icon" style="left:812px;top:313px" viewBox="0 0 28 28" aria-hidden="true">
      <path d="M14 2 L26 14 L14 26 L2 14 Z" fill="#fff" stroke="#e9a3a3" stroke-width="1.5"/>
    </svg>
    <svg class="icon" style="left:845px;top:313px" viewBox="0 0 28 28" aria-hidden="true">
      <path d="M14 2 L26 14 L14 26 L2 14 Z" fill="#fff" stroke="#e05050" stroke-width="1.5"/>
      <rect x="12.8" y="8" width="2.4" height="9" fill="#111"/>
      <circle cx="14" cy="20" r="1.5" fill="#111"/>
    </svg>

    <div class="age-mark" style="left:797px;top:349px">18+</div>
    <div class="age-mark" style="left:839px;top:349px">21+</div>
    <p class="age-note">You must be 18 years old or<br>of the legal smoking age in<br>your jurisdiction</p>

    <div class="flag-art" role="img" aria-label="United States flag"></div>
    <p class="origin">MADE IN USA</p>
  </div>
</div>
</body>
</html>
```